Buch-/eBook-Cover für Esoterikbuch
Alle meine Änderungswünsche wurden zeitnah umgesetzt. Als es nach der Dateiübergabe technische Probleme gab, weil ich den Buchinhalt falsch formatiert hatte, hat die Designerin viel Geduld bewiesen und das Cover dann klaglos an die neuen Formate angepasst. Ich werde jederzeit gerne wieder mit ihr zusammenarbeiten.
Zielgruppe
Ebook- und Taschenbuchcover für ein Esoterikbuch über Quantenheilung auf Vendura. Details befinden sich im Anhang.
Aufgabenstellung
Keine besonderen Vorgaben.

```html
<!DOCTYPE html>
<html lang="de">
<head>
<meta charset="utf-8">
<title>Quantenheilung und Bewusstsein – Buchcover</title>
<link href="https://fonts.googleapis.com/css2?family=Playfair+Display:wght@800;900&family=Noto+Serif:wght@400&family=Roboto+Mono:wght@700&display=swap" rel="stylesheet">
<style>
  :root {
    --page: #ffffff;
    --ink: #000000;
    --night: #05070f;
    --night-blue: #101a33;
    --title-white: #ffffff;
    --title-cream: #f6f0b0;
    --text: #f2f2f2;
    --glow-gold: #e9c65a;
    --glow-pink: #e86aa8;
    --glow-violet: #7a4fc9;
    --glow-cyan: #6cc8f0;
  }
  html, body {
    margin: 0;
    width: 1200px;
    height: 1200px;
    overflow: hidden;
    background: var(--page);
  }
  .canvas {
    position: relative;
    width: 1200px;
    height: 1200px;
  }
  .cover-wrap {
    position: absolute;
    left: 97px;
    top: 208px;
    width: 1014px;
    height: 791px;
    background: var(--ink);
    overflow: hidden;
  }
  .front-panel {
    position: absolute;
    left: 519px;
    top: 0;
    width: 495px;
    height: 791px;
    background:
      radial-gradient(ellipse at 30% 20%, var(--night-blue) 0%, transparent 60%),
      radial-gradient(ellipse at 80% 40%, #0d1530 0%, transparent 55%),
      var(--night);
  }
  .artwork-head {
    position: absolute;
    left: -25px;
    top: 304px;
    width: 520px;
    height: 487px;
    background:
      radial-gradient(ellipse 38% 30% at 55% 42%, rgba(200,170,255,0.85) 0%, rgba(232,106,168,0.6) 40%, rgba(122,79,201,0.3) 70%, transparent 100%),
      radial-gradient(ellipse 60% 55% at 65% 60%, rgba(233,198,90,0.18) 0%, transparent 80%);
  }
  .artwork-clouds {
    position: absolute;
    left: 3px;
    top: 511px;
    width: 206px;
    height: 280px;
    background:
      radial-gradient(ellipse 60% 45% at 45% 40%, rgba(232,106,168,0.7) 0%, rgba(122,79,201,0.45) 50%, transparent 100%),
      radial-gradient(ellipse 55% 40% at 55% 80%, rgba(246,240,176,0.75) 0%, rgba(233,198,90,0.3) 55%, transparent 100%);
  }
  .author-photo {
    position: absolute;
    left: 41px;
    top: 449px;
    width: 106px;
    height: 141px;
    background: linear-gradient(180deg, #c9d4d9 0%, #8b8f8a 45%, #4d5560 100%);
  }
  .blurb {
    position: absolute;
    left: 41px;
    top: 176px;
    width: 420px;
    margin: 0;
    font-family: "Noto Serif", serif;
    font-size: 14.4px;
    line-height: 18.2px;
    color: var(--text);
  }
  .bio {
    position: absolute;
    left: 159px;
    top: 440px;
    width: 300px;
    margin: 0;
    font-family: "Noto Serif", serif;
    font-size: 12.9px;
    line-height: 16.5px;
    color: var(--text);
  }
  .barcode-space {
    position: absolute;
    left: 287px;
    top: 678px;
    width: 154px;
    height: 87px;
    background: var(--page);
  }
  .subtitle {
    position: absolute;
    left: 0;
    top: 204px;
    width: 495px;
    margin: 0;
    text-align: center;
    font-family: "Noto Serif", serif;
    font-size: 19.5px;
    line-height: 25px;
    color: var(--text);
  }
  .type-layer {
    position: absolute;
    left: 0;
    top: 0;
  }
  .title-font { font-family: "Playfair Display", serif; font-weight: 900; }
  .spine-font { font-family: "Roboto Mono", monospace; font-weight: 700; }
</style>
</head>
<body>
<div class="canvas">
  <div class="cover-wrap">
    <section class="back-panel">
      <div class="artwork-clouds" role="img" aria-label="Farbige Nebelwolken in Pink, Violett und Gelb, die ein Profil formen"></div>
      <p class="blurb">Willkommen in der subatomaren Welt aus Quarks und Strings, wo reines Bewusstsein und reine Informationen unabhängig von Zeit und Raum das Dasein bestimmen. Seit Jahrhunderten wird die Quantenheilung erfolgreich praktiziert, wenn auch unter anderem Namen. Erst in den letzten Jahren ist es der Wissenschaft gelungen, die Wirkungsweise dieser uralten Heilungsmethode mit modernen Erkenntnissen aus der Quantenphysik in Verbindung zu bringen. Die daraus resultierenden Schlussfolgerungen und erweiterten Heilungstechniken wird dieses Buch Ihnen unter Bezug auf wissenschaftliche Methodik und Verfahrensweisen ausführlich darlegen.</p>
      <div class="author-photo" role="img" aria-label="Porträtfoto des Autors im Freien"></div>
      <p class="bio">Konrad Feldhüter wurde 1974 in Frankfurt am Main geboren. Den Fußstapfen seines Vaters folgend, hat er 2001 sein Studium der Psychologie erfolgreich abgeschlossen. Heute lebt er mit seiner Frau und seinen zwei Kindern im ländlichen Vogelsberg in der Mitte von Hessen, wo er eine kleine Praxis sowie geisteswissenschaftliche Forschung betreibt. Nach der erfolgreichen Veröffentlichung mehrerer Artikel in Fachzeitschriften hat er mit dem Schreiben und der mehrsprachigen Veröffentlichung von Büchern begonnen.</p>
      <div class="barcode-space"></div>
    </section>

    <section class="front-panel">
      <div class="artwork-head" role="img" aria-label="Leuchtendes Kopfprofil aus farbigem Sternennebel mit goldenen Lichtlinien"></div>
      <p class="subtitle">Wie Sie Zugriff auf die Informationsebene<br>der Realität nehmen</p>
    </section>

    <svg class="type-layer" width="1014" height="791" viewBox="0 0 1014 791" aria-hidden="false">
      <g class="title-font">
        <text x="35" y="105" font-size="58" fill="var(--title-white)" textLength="423" lengthAdjust="spacingAndGlyphs">QUANTENHEILUNG</text>
        <text x="36" y="160" font-size="54" fill="var(--title-cream)" textLength="420" lengthAdjust="spacingAndGlyphs">UND BEWUSSTSEIN</text>
        <text x="555" y="117" font-size="56" fill="var(--title-white)" textLength="422" lengthAdjust="spacingAndGlyphs">QUANTENHEILUNG</text>
        <text x="557" y="171" font-size="52" fill="var(--title-cream)" textLength="418" lengthAdjust="spacingAndGlyphs">UND BEWUSSTSEIN</text>
        <text x="600" y="742" font-size="31" font-weight="800" fill="var(--title-white)" textLength="333" lengthAdjust="spacingAndGlyphs">KONRAD FELDHÜTER</text>
      </g>
      <text class="spine-font" x="0" y="0" font-size="12" fill="var(--title-white)" transform="translate(503 133) rotate(90)" textLength="521" lengthAdjust="spacing">QUANTENHEILUNG und BEWUSSTSEIN</text>
    </svg>
  </div>
</div>
</body>
</html>
```